Coffee Roastery Label Sticker Design

We are starting a small Micro-Coffee-Roastery and are looking for a catchy design, which might look a bit hipster style, but not too much. It's called "pebble kilnhouse", because we started roasting first in our backyard / garden by our house.
At the end of the logo and the details of the sticker (like all text elements) we need to be able to modify later by ourselfs. Coffee type, origin of coffee and so one ...
The label will be sticked on a white craftpaper coffee bag of 250grams. Sticker size around 8x12.5 cm.
The coffee bag should be an eye-catcher in a shop-shelve compared to the other coffee brands.
Another example that i really like (just to get you another idea of what we would love to get because we really like that style): https://pixvaultcdn.net/design_img/5719204/83051/61730482/qwmrlezt4k7b9d1pf2hyv8nusa_image.png).
OR https://packframe.net/blog/2016/3/14/larkhill-coffee?

Target Market(s)

"0Speciality Coffee" lovers
High quality specialty coffee and a clear origin of the bean and fair trade or project coffee is what makes our roasted coffee product special

Logo Text

Kiesel Brennerei

Requirements
Must have
• A house and a garden with either flowers or a tree is what we have in mind.
The printed label will be square 8x12.5 cm. We will use the logo on the printed label (we will print on our own printer) and on a homepage.
Nice to have
• In the attached logo example, there is no connection to a coffee business. Actually it would be a nice detail to include somehow either a descent coffee bean, a cup or a tiny roastery machine or whatever is in your mind with coffee ... (not a grinder)
Black and white is OK, but we also like colourfull very much
Please see the attached documents with sample designs that we created on our own with canvas. It's not too bad, but also a bit boring. If you have a completely different idea, please go for it. we are very open for other cool and hip designs or also quite descent and femail touch is fine too, but no must.

```html
<!DOCTYPE html>
<html lang="de">
<head>
<meta charset="utf-8">
<title>Kiesel Brennerei – Speciality Coffee Label</title>
<link rel="stylesheet" href="https://fonts.googleapis.com/css2?family=Yanone+Kaffeesatz:wght@400;600&display=swap">
<style>
  :root {
    --canvas: #f4f4f2;
    --label-white: #ffffff;
    --teal: #7fcfc3;
    --teal-soft: #a9e0d7;
    --teal-deep: #68c0b3;
    --text-light: #ffffff;
    --rule: rgba(255, 255, 255, 0.85);
  }
  * { margin: 0; padding: 0; box-sizing: border-box; }
  html, body {
    width: 1200px;
    height: 1200px;
    overflow: hidden;
    background: var(--canvas);
  }
  .canvas {
    width: 1200px;
    height: 1200px;
    display: flex;
    align-items: center;
    justify-content: center;
  }
  .label {
    width: 640px;
    height: 880px;
    background: var(--label-white);
    box-shadow: 0 2px 10px rgba(0, 0, 0, 0.08);
    display: flex;
    flex-direction: column;
    font-family: "Yanone Kaffeesatz", "Arial Narrow", sans-serif;
  }
  .brand {
    height: 360px;
    display: flex;
    flex-direction: column;
    align-items: center;
    justify-content: center;
    gap: 26px;
  }
  .brand-mark {
    width: 170px;
    height: 170px;
    border-radius: 50%;
    background: radial-gradient(circle at 50% 45%, var(--teal-soft), var(--teal));
  }
  .brand-name {
    font-weight: 600;
    font-size: 64px;
    letter-spacing: 4px;
    color: var(--teal-deep);
    text-transform: uppercase;
  }
  .details {
    flex: 1;
    background: linear-gradient(180deg, var(--teal-soft) 0%, var(--teal) 35%, var(--teal) 100%);
    color: var(--text-light);
    padding: 48px 56px 40px;
    display: flex;
    flex-direction: column;
  }
  .category {
    font-weight: 600;
    font-size: 58px;
    letter-spacing: 2px;
    text-transform: uppercase;
    text-align: center;
    padding-bottom: 10px;
    border-bottom: 2px solid var(--rule);
  }
  .product {
    margin-top: 14px;
    width: 74%;
    align-self: center;
    font-weight: 400;
    font-size: 40px;
    line-height: 1.05;
    letter-spacing: 1.5px;
    text-transform: uppercase;
    padding-bottom: 12px;
    border-bottom: 2px solid var(--rule);
  }
  .facts {
    list-style: none;
    margin-top: 22px;
    align-self: flex-end;
    width: 52%;
    font-weight: 400;
    font-size: 22px;
    line-height: 1.45;
    letter-spacing: 1px;
    text-transform: uppercase;
  }
</style>
</head>
<body>
  <main class="canvas">
    <article class="label">
      <header class="brand">
        <div class="brand-mark" aria-hidden="true"></div>
        <h1 class="brand-name">Kiesel Brennerei</h1>
      </header>
      <section class="details">
        <h2 class="category">Speciality Coffee</h2>
        <p class="product">Filterkaffee<br>Äthiopien – Guji</p>
        <ul class="facts">
          <li>250 Gramm</li>
          <li>Helle Röstung</li>
          <li>Kaffee aus Äthiopien</li>
          <li>100% Arabica | Washed</li>
          <li>Geröstet in 4417 Kieseltal</li>
          <li>www.kiesel-brennerei.ch</li>
        </ul>
      </section>
    </article>
  </main>
</body>
</html>
```